New design for PeopleDeskly

We are at the start of the process of evolving an existing business, and have just developed a new logo that will guide the look and feel of the rest of the site.

PeopleDeskly.com.au will be the place to go for small business owners that need guidance and tools on how to look after HR functions such as recruitment and performance management amongst other aspects.

The existing site that is going to be evolved in www.staffingpathguide.com.au - while some of the content will remain, the entire look of the site needs to change, and a new homepage and other pages need to be developed.

For this project, we'd like the new homepage to be designed to lead the way for how the rest of the pages will look moving forward.

We're looking for a clean, clear and modern design. It should not feel cluttered or busy

The wireframe for the new homepage, and another landing page are attached.

Target Market(s)

Small and medium business owners - slightly male skew

Industry/Entity Type

Small Business

Requirements
Must have
• - Should be clean and simple
- The overall feel from the new logo (attached to the project) should be integrated into all elements of the site
- Should communicate that the site is easy to navigate
- Should communicate that the site is friendly and approachable
- Should communicate that the site is professional (for small businesses)
Nice to have
• This homepage for this site is quite a good design reference in terms of clean design.

http://www.chorebadger.example/

For PeopleDeskly though, the 3 boxes under the main image should appear above the fold though.

Also, happy for one other colour to be introduced to highlight call to action buttons etc.
Should not have
• Must not be cluttered
Should not introduce more than one additional colour to the existing colours from the logo

```html
<!DOCTYPE html>
<html lang="en">
<head>
<meta charset="utf-8">
<title>PeopleDeskly – Product Suite</title>
<link href="https://fonts.googleapis.com/css2?family=Source+Sans+3:wght@400;600;700&display=swap" rel="stylesheet">
<style>
:root{
  --blue:#1a68b3;
  --blue-dark:#0f5aa6;
  --blue-light:#3b9ee2;
  --panel:#cfe1f0;
  --panel-line:#9cc3e3;
  --orange:#f07a1e;
  --orange-dark:#e0600c;
  --text:#3a3a3a;
  --band:#dde9f4;
  --white:#ffffff;
}
*{box-sizing:border-box;margin:0;padding:0}
html,body{width:1200px;height:844px;overflow:hidden}
body{font-family:"Source Sans 3",sans-serif;color:var(--text);
  background:linear-gradient(#dce8f3 0,#ffffff 60px,#ffffff 100%);position:relative}
.abs{position:absolute}
.brand{left:168px;top:26px;display:flex;align-items:center;gap:8px}
.brand-dot{width:34px;height:34px;border-radius:50%;background:var(--blue)}
.brand-name{font-size:30px;font-weight:700;color:var(--blue);letter-spacing:-.5px}
.suite-name{left:198px;top:75px;font-size:14px;color:var(--blue)}
.search{left:821px;top:36px;width:216px;height:30px;border:1px solid #aab;border-radius:3px;background:#fff;
  font-size:12px;color:#5a86b8;padding:7px 10px}
.search svg{position:absolute;right:8px;top:6px}
.nav{left:163px;top:98px;width:875px;height:31px;display:flex;border-radius:3px;overflow:hidden;
  background:linear-gradient(var(--blue-light),var(--blue-dark))}
.nav a{color:#fff;text-decoration:none;font-size:12.5px;display:flex;align-items:center;justify-content:center;
  border-right:1px solid #1d5e9c}
.nav a:last-child{border-right:0}
.nav a.active{background:linear-gradient(#9a9a9a,#3e3e3e)}
.steps{left:174px;top:152px;width:253px;height:292px;background:var(--panel);border:1px solid var(--panel-line);
  border-radius:3px;padding:18px 17px}
.steps h2{font-size:17px;font-weight:700;color:var(--blue);padding-bottom:9px;border-bottom:1px solid #a9c4da}
.steps ul{list-style:none}
.steps li{height:37px;border-bottom:1px solid #a9c4da;display:flex;align-items:center;font-size:13px;color:var(--blue)}
.steps li:last-child{border-bottom:0}
.steps li svg{margin:0 12px 0 -2px}
.card{background:linear-gradient(#fff,#f1f6fb);border:1px solid #c9d8e6;border-radius:3px;box-shadow:2px 3px 4px rgba(0,0,0,.12)}
.video-card{left:440px;top:154px;width:587px;height:289px}
.card-title{font-size:17px;color:var(--blue);position:absolute}
.dots{position:absolute;border-bottom:2px dotted #6f8aa8;height:0}
.intro{left:14px;top:50px;width:165px;height:227px;background:#e8f3fc;border:1px solid #b9d5ec;border-radius:3px;padding:12px 10px}
.intro h3{font-size:12px;font-weight:400;color:var(--blue);margin-bottom:9px}
.intro p{font-size:9.5px;line-height:18.5px;text-align:justify;color:#333;margin-bottom:10px}
.hl{color:var(--orange)}
.intro .more{text-align:right;font-size:9.5px;color:#222}
.player{left:196px;top:52px;width:374px;height:222px;background:linear-gradient(#56687a,#3a4b5c 60%,#8d9aa6);overflow:hidden}
.controls{left:8px;bottom:8px;width:358px;height:32px;background:rgba(30,35,40,.8);border-radius:3px}
.time{left:67px;top:-12px;background:#fff;color:#222;font-size:10px;font-weight:700;padding:1px 3px;border-radius:2px}
.kit{left:173px;top:466px;width:855px;height:207px}
.kit p{font-size:11.5px;line-height:18.5px;color:#333}
.kit-text{left:17px;top:50px;width:575px}
.photo{left:608px;top:53px;width:236px;height:86px;background:linear-gradient(100deg,#d9d4c8,#b9c9d6 55%,#e9e5dc);border:1px solid #9aa}
.btn{height:26px;border-radius:3px;background:linear-gradient(#f6913a,var(--orange-dark));color:#fff;font-size:13px;
  display:flex;align-items:center;gap:8px;padding-left:15px;top:159px;box-shadow:1px 2px 3px rgba(0,0,0,.2)}
.footer{left:0;top:695px;width:1200px;height:149px;background:linear-gradient(var(--band),#fff 60px)}
.links{top:19px;width:1200px;display:flex;justify-content:center;gap:19px;font-size:12px;color:var(--blue)}
.links span.sep{color:var(--blue)}
.addr{top:53px;width:1200px;text-align:center;font-size:11.5px;color:#333;line-height:20px}
.rule{left:162px;top:99px;width:921px;border-top:1px solid #c8d9e8}
.copy{top:115px;width:1200px;text-align:center;font-size:11.5px;color:#333}
</style>
</head>
<body>
<div class="abs brand"><span class="brand-dot"></span><span class="brand-name">PeopleDeskly</span></div>
<div class="abs suite-name">[Product Suit Name]</div>
<div class="abs search">Search
  <svg width="18" height="18" viewBox="0 0 18 18"><circle cx="7" cy="7" r="5" fill="none" stroke="#888" stroke-width="2"/><line x1="11" y1="11" x2="16" y2="16" stroke="#777" stroke-width="3"/></svg>
</div>
<nav class="abs nav">
  <a class="active" style="width:95px">Attract</a><a style="width:83px">Recruit</a><a style="width:90px">Induction</a>
  <a style="width:87px">Engage</a><a style="width:111px">Performance</a><a style="width:170px">Termination &amp; Community</a>
  <a style="width:114px">Management</a><a style="width:125px">Redundancy</a>
</nav>

<aside class="abs steps">
  <h2>How to [ Product Suit Name ]</h2>
  <ul>
    <li><svg width="10" height="10" viewBox="0 0 10 10"><path d="M1 5l3 3 5-7" fill="none" stroke="#555" stroke-width="1.8"/></svg>Lorem ipsum</li>
    <li><svg width="10" height="10" viewBox="0 0 10 10"><path d="M1 5l3 3 5-7" fill="none" stroke="#555" stroke-width="1.8"/></svg>Lorem ipsum text</li>
    <li><svg width="10" height="10" viewBox="0 0 10 10"><path d="M1 5l3 3 5-7" fill="none" stroke="#555" stroke-width="1.8"/></svg>Lorem ipsum simple</li>
    <li><svg width="10" height="10" viewBox="0 0 10 10"><path d="M1 5l3 3 5-7" fill="none" stroke="#555" stroke-width="1.8"/></svg>Lorem ipsum simple text</li>
    <li><svg width="10" height="10" viewBox="0 0 10 10"><path d="M1 5l3 3 5-7" fill="none" stroke="#555" stroke-width="1.8"/></svg>Lorem ipsum dummy text</li>
    <li><svg width="10" height="10" viewBox="0 0 10 10"><path d="M1 5l3 3 5-7" fill="none" stroke="#555" stroke-width="1.8"/></svg>Lorem ipsum text simple</li>
  </ul>
</aside>

<section class="abs card video-card">
  <h2 class="card-title" style="left:16px;top:11px">Step 1 Video</h2>
  <div class="dots" style="left:18px;top:40px;width:236px"></div>
  <div class="abs intro">
    <h3>Lorem ipsum</h3>
    <p>Lorem Ipsum is <span class="hl">simply dummy text</span> of the printing and typesetting industry. Lorem Ipsum has been the industry's standard...</p>
    <p>Lorem Ipsum is <span class="hl">simply dummy text</span> of the printing and typesetting industry. Lorem Ipsum has been the industry's standard...</p>
    <div class="more">Read more...</div>
  </div>
  <div class="abs player" role="img" aria-label="Video still of a presenter in a studio with screens behind her">
    <div class="abs controls">
      <svg class="abs" style="left:22px;top:8px" width="18" height="18" viewBox="0 0 18 18"><path d="M2 1l15 8-15 8z" fill="#fff"/></svg>
      <div class="abs" style="left:85px;top:12px;width:185px;height:8px;border:1px solid #888;border-radius:2px"></div>
      <span class="abs time">00:36</span>
      <svg class="abs" style="left:278px;top:10px" width="34" height="12"><g fill="#29a8e6"><rect x="0" width="2" height="12"/><rect x="5" width="2" height="12"/><rect x="10" width="2" height="12"/><rect x="15" width="2" height="12"/><rect x="20" width="2" height="12"/><rect x="25" width="2" height="12"/><rect x="30" width="2" height="12"/></g></svg>
      <span class="abs" style="left:320px;top:6px;color:#888;font-weight:700;font-style:italic;font-size:14px">HD</span>
      <svg class="abs" style="left:345px;top:10px" width="12" height="12" viewBox="0 0 12 12"><path d="M1 4V1h3M8 1h3v3M11 8v3H8M4 11H1V8" fill="none" stroke="#999" stroke-width="1.5"/></svg>
    </div>
  </div>
</section>

<section class="abs card kit">
  <h2 class="card-title" style="left:17px;top:11px">View free information and the [productsuite] kit that will support your end-to-end [xxx] process</h2>
  <div class="dots" style="left:19px;top:41px;width:838px"></div>
  <div class="abs kit-text">
    <p>Lorem Ipsum is <span class="hl">simply dummy text</span> of the printing and typesetting industry. Lorem Ipsum has been the industry's standard...</p>
    <p>Lorem Ipsum is simply dummy text of the printing and typesetting industry. Lorem Ipsum has been the industry's standard dummy text ever since the 1500s, when an unknown printer took a galley of type and scrambled it to make a type specimen book</p>
  </div>
  <div class="abs photo" role="img" aria-label="Photo of three colleagues talking at an office desk"></div>
  <a class="abs btn" style="left:19px;width:140px">Free Information <svg width="13" height="13" viewBox="0 0 13 13"><circle cx="6.5" cy="6.5" r="5.5" fill="none" stroke="#fff" stroke-width="1.3"/><path d="M5 3.8l3 2.7-3 2.7" fill="none" stroke="#fff" stroke-width="1.5"/></svg></a>
  <a class="abs btn" style="left:254px;width:121px">Full Kit $ 299 <svg width="13" height="13" viewBox="0 0 13 13"><circle cx="6.5" cy="6.5" r="5.5" fill="none" stroke="#fff" stroke-width="1.3"/><path d="M5 3.8l3 2.7-3 2.7" fill="none" stroke="#fff" stroke-width="1.5"/></svg></a>
  <a class="abs btn" style="left:461px;width:126px">Ind. Step $ 99 <svg width="13" height="13" viewBox="0 0 13 13"><circle cx="6.5" cy="6.5" r="5.5" fill="none" stroke="#fff" stroke-width="1.3"/><path d="M5 3.8l3 2.7-3 2.7" fill="none" stroke="#fff" stroke-width="1.5"/></svg></a>
</section>

<footer class="abs footer">
  <div class="abs links"><span>Privacy Policy</span><span class="sep">|</span><span>Terms &amp; Conditions</span><span class="sep">|</span><span>Sitemap</span><span class="sep">|</span><span>Contact</span><span class="sep">|</span><span>Your Feedback</span></div>
  <div class="abs addr">Level 4, 22 Harbourline Street, SYDNEY NSW 2000, Phone: (02) 9000 4812<br>Email: info@staffingpathguide.com.au</div>
  <div class="abs rule"></div>
  <div class="abs copy">Copyrights @ 2012 All Rights Reserved</div>
</footer>
</body>
</html>
```